Brochure for Saltmoss Drift Outings

A new brochure/A4 Flyer for our Saltmoss Drift Outings.
We have been operating a successful small business for 3 years in The Whisundays, QLD, Australia. The heart of the Great Barrier Reef.
We offer one-hour Saltmoss Drift Outings 3 times a day on our zero emissions electric boat for up to 8 guests.

Target Market(s)

All tourists visiting the Whitsundays. All ages and abilities

Industry/Entity Type

Tourism

Font styles to use
Other font styles liked:
• Easy to read

Colors
0054AA
0677BA
7BADD7
CADEEF
E8F1F8
00AB8E
00BBA5
67D7C9
C6EFE9
E9F9F6

Requirements
Must have
• High impact font page. It's all about Kelpwind Trips for one-hour.
Nice to have
• Kelpwind Trips in top quarter/third of front page with a picture of a turtle
Should not have
• Not too much distraction on front page. More info on the back

```html
<!DOCTYPE html>
<html lang="en">
<head>
<meta charset="utf-8">
<title>Hushwater Cruises – Kelpwind Trips Flyer</title>
<link rel="stylesheet" href="https://fonts.googleapis.com/css2?family=Bebas+Neue&family=Quicksand:wght@500;600;700&family=Poppins:ital,wght@0,400;0,700;0,800;1,400;1,700;1,800&display=swap">
<style>
  :root {
    --stage: #2a2f38;
    --sky: #46d0fd;
    --sky-deep: #2fb6ee;
    --ocean: #1579c9;
    --navy: #0d4ea5;
    --ink: #16306b;
    --white: #ffffff;
    --teal: #00ab8e;
    --teal-light: #00bba5;
    --photo-a: #1c6fb8;
    --photo-b: #0b3f7d;
  }
  * { box-sizing: border-box; margin: 0; padding: 0; }
  html, body { width: 1200px; height: 836px; overflow: hidden; background: var(--stage); }
  .canvas { position: relative; width: 1200px; height: 836px; }

  .page { position: absolute; top: 30px; width: 548px; height: 776px; background: var(--sky); overflow: hidden; }
  .page--front { left: 37px; }
  .page--back { left: 618px; }

  /* Front */
  .front-photo { position: absolute; left: 0; top: 0; width: 100%; height: 300px;
    background: linear-gradient(180deg, #1d86cc 0%, #0f5fae 60%, #0b4d98 100%); }
  .front-wave { position: absolute; left: 0; top: 268px; width: 100%; height: 60px; }
  .brand { position: absolute; left: 0; width: 100%; text-align: center;
    font-family: "Quicksand", sans-serif; font-weight: 700; color: var(--white); }
  .front .brand { top: 262px; font-size: 40px; letter-spacing: 1px; line-height: 1; }
  .brand-sub { display: block; font-size: 17px; letter-spacing: 8px; margin-top: 8px; }
  .headline { position: absolute; left: 0; width: 100%; text-align: center;
    font-family: "Bebas Neue", sans-serif; color: var(--navy); line-height: 0.92; }
  .headline--main { top: 330px; font-size: 78px; }
  .headline--sub { top: 410px; font-size: 50px; }
  .rule { position: absolute; left: 105px; width: 338px; border-top: 1.5px dotted var(--ink); }
  .tagline { position: absolute; left: 0; width: 100%; top: 534px; text-align: center;
    font-family: "Quicksand", sans-serif; font-weight: 600; font-size: 22px; line-height: 1.12; color: var(--ink); }
  .times { position: absolute; left: 0; width: 100%; top: 605px; text-align: center;
    font-family: "Bebas Neue", sans-serif; font-size: 41px; color: var(--navy); letter-spacing: -0.3px; }
  .location { position: absolute; left: 0; width: 100%; top: 654px; text-align: center;
    font-family: "Quicksand", sans-serif; font-weight: 700; font-size: 18px; letter-spacing: 1px; color: var(--white); }
  .web { position: absolute; left: 0; width: 100%; top: 694px; text-align: center;
    font-family: "Quicksand", sans-serif; font-weight: 600; font-size: 18px; color: var(--ink); }
  .book { position: absolute; left: 0; width: 100%; text-align: center;
    font-family: "Poppins", sans-serif; color: var(--white); white-space: nowrap; }
  .front .book { top: 734px; font-size: 17px; }
  .book strong { font-weight: 800; margin-right: 22px; }
  .book span { font-family: "Quicksand", sans-serif; font-weight: 500; }

  /* Back */
  .back-photo { position: absolute; left: 0; top: 0; width: 100%; height: 270px;
    background: linear-gradient(180deg, #4f7a62 0%, #3f7f8e 45%, #2aa0c0 100%); }
  .back-wave { position: absolute; left: 0; top: 232px; width: 100%; height: 60px; }
  .back-photo .brand { top: 170px; font-size: 28px; }
  .back-photo .brand-sub { font-size: 11px; letter-spacing: 5px; margin-top: 4px; }
  .eyebrow { position: absolute; left: 0; width: 100%; top: 272px; text-align: center;
    font-family: "Poppins", sans-serif; font-weight: 700; color: var(--white); line-height: 1.3; }
  .eyebrow small { display: block; font-size: 10.5px; }
  .eyebrow b { display: block; font-size: 14px; font-weight: 800; letter-spacing: 0.3px; }
  .tour-card { position: absolute; top: 311px; height: 123px; background: var(--navy); border-radius: 20px;
    display: flex; align-items: center; justify-content: center; text-align: center; padding: 0 10px;
    font-family: "Poppins", sans-serif; font-style: italic; font-weight: 800; font-size: 9.8px; line-height: 1.45; color: var(--white); }
  .tour-card--mimosa { left: 31px; width: 149px; }
  .tour-card--hour { left: 204px; width: 148px; }
  .tour-card--sunset { left: 377px; width: 140px; }
  .meet { position: absolute; left: 20px; width: 508px; top: 438px; text-align: center;
    font-family: "Poppins", sans-serif; font-style: italic; font-size: 10.5px; line-height: 1.35; color: var(--ink); }
  .group-photo { position: absolute; left: 0; top: 466px; width: 100%; height: 139px;
    clip-path: polygon(0 0, 100% 15px, 100% 100%, 0 97%);
    background: linear-gradient(100deg, #d9c3a4 0%, #b88c6a 40%, #8a6a52 70%, #e0d6cb 100%); }
  .story { position: absolute; left: 18px; width: 512px; top: 612px; text-align: center;
    font-family: "Poppins", sans-serif; font-size: 7.2px; line-height: 1.38; color: var(--white); }
  .story p + p { margin-top: 9px; }
  .challenge { position: absolute; left: 0; width: 100%; top: 697px; text-align: center;
    font-family: "Poppins", sans-serif; font-weight: 800; font-size: 13.5px; letter-spacing: 0.4px; color: var(--white); }
  .footer-wave { position: absolute; left: 0; top: 718px; width: 100%; height: 58px; }
  .back .book { top: 742px; font-size: 18px; }
  .badge { position: absolute; left: 474px; top: 710px; width: 52px; height: 44px;
    background: var(--navy); border-radius: 22px 18px 24px 14px; }
</style>
</head>
<body>
<main class="canvas">

  <section class="page page--front front">
    <div class="front-photo" role="img" aria-label="Photo of a sea turtle swimming in clear blue water"></div>
    <svg class="front-wave" viewBox="0 0 548 60" preserveAspectRatio="none" aria-hidden="true">
      <path d="M0 18 C60 4 110 30 170 16 S290 4 350 18 S470 30 548 10 V60 H0Z" fill="var(--sky-deep)"/>
      <path d="M0 32 C70 20 130 42 200 30 S330 18 400 32 S500 38 548 26 V60 H0Z" fill="var(--sky)"/>
    </svg>
    <div class="brand">Hushwater<span class="brand-sub">CRUISES</span></div>

    <h1 class="headline headline--main">KELPWIND TRIPS</h1>
    <h2 class="headline headline--sub">ONE HOUR SALTMOSS<br>DRIFT OUTINGS</h2>

    <div class="rule" style="top:521px"></div>
    <p class="tagline">3 TIMES A DAY ON OUR ZERO EMISSIONS<br>ELECTRIC BOAT FOR UP TO 8 GUESTS</p>
    <div class="rule" style="top:596px"></div>
    <p class="times">DAILY AT 9.30AM, 11.00AM &amp; 12.30PM</p>
    <p class="location">AIRLIE BEACH</p>
    <div class="rule" style="top:685px"></div>
    <p class="web">www.hushwatercruises.com.au</p>
    <div class="rule" style="top:722px"></div>
    <p class="book"><strong>BOOK NOW</strong><span>0400 512 736</span></p>
  </section>

  <section class="page page--back back">
    <div class="back-photo" role="img" aria-label="Photo of guests aboard the covered electric boat on calm water near green hills">
      <div class="brand">Hushwater<span class="brand-sub">CRUISES</span></div>
    </div>
    <svg class="back-wave" viewBox="0 0 548 60" preserveAspectRatio="none" aria-hidden="true">
      <path d="M0 20 C80 2 160 6 240 14 S400 28 470 14 S530 4 548 8 V60 H0Z" fill="var(--sky)"/>
    </svg>

    <div class="eyebrow"><small>PRIVATE CHARTERS AVAILABLE</small><b>TOURS AVAILABLE DAILY</b></div>

    <div class="tour-card tour-card--mimosa">Mimosa Morning<br>Cruise<br>9.30am - $85pp<br>Includes<br>Mimosas/Orange<br>Juice/Bubbles</div>
    <div class="tour-card tour-card--hour">One-Hour Saltmoss<br>Drift Outings<br>operate daily at<br>11:00am and 12.30pm<br>$69pp adults (16+)<br>$55pp child (1-15yo)<br>Infants FOC (0-1)</div>
    <div class="tour-card tour-card--sunset">Sunset Saltmoss<br>Drift Outing<br>Duration: 1.5 hours<br>Available for<br>Private<br>Charter Only</div>

    <p class="meet">Meet outside Marlowe Bar &amp; Restaurant, Palm Reach Marina (North Complex) 10 minutes prior to departure. Maximum 8 guests.</p>

    <div class="group-photo" role="img" aria-label="Photo of a smiling group of guests seated on the boat at sunset"></div>

    <div class="story">
      <p>Embark on an extraordinary and environmentally responsible journey by stepping aboard Airlie Beach's most unique tour. Join us for an intimate and serene adventure where sustainability meets luxury, creating memories that are as gentle on the environment as they are unforgettable.</p>
      <p>With a maximum capacity of just 8 passengers, our charming vessel 'Wren' stands out as the only electric boat in the Whitsundays. Experience the magic of spotting turtles in eco-friendly luxury, gliding though calm waters with our whisper-quiet, fume-free electric boat. Be on the lookout for the endangered loggerhead and green sea turtles. Immerse yourself in a serene journey as we tour through Turtle Bay, around Pigeon Island and the local foreshore, then back past the million-dollar yachts in the Palm Reach Marina.</p>
    </div>

    <p class="challenge">CAN YOU BEAT OUR ‘TURTLE COUNT’ RECORD?</p>

    <svg class="footer-wave" viewBox="0 0 548 58" preserveAspectRatio="none" aria-hidden="true">
      <path d="M0 14 C90 0 170 4 260 14 S420 26 548 6 V58 H0Z" fill="var(--teal)"/>
    </svg>
    <div class="badge" aria-hidden="true"></div>
    <p class="book"><strong>BOOK NOW</strong><span>0400 512 736</span></p>
  </section>

</main>
</body>
</html>
```